Bold Cover needed for a book on Workplace Bullying

I need a book cover design for a book titled, “Iron Silence?” The book recounts my story of bullying in the workplace. It also includes chapters on how readers can minimize/stop workplace bullying, write an effective complaint, and ensure their own mental wellbeing.
I am looking for a bold design using red and black, and possibly distressed lettering. The covers of other books dealing with this subject do not reflect my vision. They are often too childish or look too academic. This book needs to stress the serious nature of a toxic workplace, while appealing to readers experiencing a similar situation. I’d like the cover to reflect the mental anguish associated with workplace bullying (hence the distressed lettering).
I have included a cover that appeals to me (although the coloring is wrong). That said, I am also very happy (and excited) to see your creative input!
On the cover, it should have the following:
Title: Iron Silence?
Subtitle: How the Harbour Works Department Condones Bullying & Ruins Lives
Author: Owen Frick
Other relevant details:
Book size: 5.5” x 8.5”
Back cover will have a blurb, author picture/short bio, and barcode
The blurb on the back cover reads:
Undermining, intimidation and threats
Despite the Department of Harbour Works allegedly holding a zero tolerance for bullying, these behaviours were an everyday occurrence in at least one workplace. Even after a decade of complaints, numerous witnesses and physical proof, the department failed to act. Instead, they looked the other way, allowing one powerful and well-connected individual to end careers and ruin lives.
After being targeted, one teacher resolved to put an end to the abuse experienced by more than fifty employees. His startling story reveals the relentless bullying, mental health ramifications, and insidious tactics used to cover up the corrosive behaviour.
Those who have experienced a toxic workplace will also find much needed support and guidance, intended to minimise suffering and detail a clear way forward. Chapters include dealing with bullying in the workplace, how to lodge a successful complaint, and how to stay sane during any potential legal action.

```html
<!DOCTYPE html>
<html lang="en">
<head>
<meta charset="utf-8">
<title>Iron Silence? — Owen Frick</title>
<link rel="stylesheet" href="https://fonts.googleapis.com/css2?family=Anton&family=Oswald:wght@500&family=Quicksand:wght@500&display=swap">
<style>
  :root {
    --backdrop: #021b29;
    --ink: #0f1c2b;
    --red: #e8465a;
    --dot-dark: #1d2838;
    --dot-red: #d63f52;
  }
  * { margin: 0; padding: 0; box-sizing: border-box; }
  html, body {
    width: 1200px;
    height: 926px;
    overflow: hidden;
    background: var(--backdrop);
  }
  .stage {
    position: relative;
    width: 1200px;
    height: 926px;
  }
  .book-cover {
    position: absolute;
    left: 344px;
    top: 64px;
    width: 514px;
    height: 798px;
    display: block;
    filter: drop-shadow(0 18px 40px rgba(0, 0, 0, 0.55));
  }
  .panel-dark { fill: var(--ink); }
  .panel-red { fill: var(--red); }
  .title-main, .title-sub { font-family: "Anton", "Oswald", sans-serif; }
  .subtitle { font-family: "Quicksand", "Helvetica Neue", sans-serif; font-weight: 500; font-size: 17px; }
  .author { font-family: "Oswald", "Arial Narrow", sans-serif; font-weight: 500; font-size: 40px; letter-spacing: 22px; }
  .type-on-dark { fill: var(--red); }
  .type-on-red { fill: var(--ink); }
</style>
</head>
<body>
<main class="stage">
  <svg class="book-cover" viewBox="0 0 514 798" xmlns="http://www.w3.org/2000/svg" role="img" aria-label="Book cover: Iron Silence? How the Harbour Works Department Condones Bullying &amp; Ruins Lives, by Owen Frick">
    <defs>
      <clipPath id="half-left"><rect x="0" y="0" width="257" height="798"/></clipPath>
      <clipPath id="half-right"><rect x="257" y="0" width="257" height="798"/></clipPath>

      <linearGradient id="dark-tone" x1="0" y1="0" x2="0" y2="1">
        <stop offset="0" stop-color="var(--dot-dark)"/>
        <stop offset="0.35" stop-color="var(--ink)"/>
        <stop offset="0.7" stop-color="var(--ink)"/>
        <stop offset="1" stop-color="var(--dot-dark)"/>
      </linearGradient>
      <linearGradient id="red-tone" x1="0" y1="0" x2="0" y2="1">
        <stop offset="0" stop-color="var(--dot-red)"/>
        <stop offset="0.35" stop-color="var(--red)"/>
        <stop offset="0.7" stop-color="var(--red)"/>
        <stop offset="1" stop-color="var(--dot-red)"/>
      </linearGradient>

      <filter id="worn-print" x="-5%" y="-5%" width="110%" height="110%">
        <feTurbulence type="fractalNoise" baseFrequency="0.9" numOctaves="2" seed="7" result="grain"/>
        <feColorMatrix in="grain" type="matrix"
          values="0 0 0 0 0  0 0 0 0 0  0 0 0 0 0  0 0 0 -2.2 1.45" result="speckle"/>
        <feComposite in="SourceGraphic" in2="speckle" operator="in"/>
      </filter>

      <g id="cover-type">
        <g filter="url(#worn-print)">
          <text class="title-main" x="36" y="380" font-size="350" textLength="440" lengthAdjust="spacingAndGlyphs">IRON</text>
          <text class="title-sub" x="32" y="512" font-size="142" textLength="450" lengthAdjust="spacingAndGlyphs">SILENCE?</text>
        </g>
        <text class="subtitle" x="257" y="552" text-anchor="middle">How the Harbour Works Department Condones</text>
        <text class="subtitle" x="257" y="577" text-anchor="middle">Bullying &amp; Ruins Lives</text>
        <text class="author" x="268" y="746" text-anchor="middle">OWEN FRICK</text>
      </g>
    </defs>

    <rect class="panel-dark" x="0" y="0" width="257" height="798" fill="url(#dark-tone)" role="img" aria-label="Dark halftone dot texture"/>
    <rect class="panel-red" x="257" y="0" width="257" height="798" fill="url(#red-tone)" role="img" aria-label="Red halftone dot texture"/>

    <use href="#cover-type" class="type-on-dark" clip-path="url(#half-left)"/>
    <use href="#cover-type" class="type-on-red" clip-path="url(#half-right)" aria-hidden="true"/>
  </svg>
</main>
</body>
</html>
```